Business Card Design Quandong Celebration Crafters

on the front i would like to see the logo and my contact details. on the back i would like it to include the 3 parts to the business party planning, party hire and party supplies also with a line at the bottom (or white space) to write their appointment details.

Target Market(s)

mums and corporates

Industry/Entity Type

Business

Requirements
Must have
• logo and contact details which are: Name: Rosalind, Phone: 0417365920, email: ros@quandongfetes.com.au, Website: www.quandongfetes.com.au,

```html
<!DOCTYPE html>
<html lang="en">
<head>
<meta charset="utf-8">
<title>Quandong Celebration Crafters – Business Card</title>
<link rel="stylesheet" href="https://fonts.googleapis.com/css2?family=Montserrat:wght@600;700;800&family=Lato:wght@400;700&display=swap">
<style>
  :root {
    --purple: #5a3ea6;
    --purple-deep: #4b3196;
    --cyan: #2db9de;
    --yellow: #f5c31c;
    --magenta: #b5439b;
    --ink: #3a3a3a;
    --rule: #d6d6d6;
    --paper: #ffffff;
    --stage: #ecebef;
  }
  * { box-sizing: border-box; margin: 0; padding: 0; }
  html, body { width: 1200px; height: 840px; overflow: hidden; }
  body {
    background: var(--stage);
    position: relative;
    font-family: "Lato", Arial, sans-serif;
  }

  .card { position: absolute; border-radius: 4px; overflow: hidden; box-shadow: 0 6px 18px rgba(40,30,80,.15); }

  /* Front */
  .card-front {
    left: 141px; top: 160px; width: 318px; height: 520px;
    background: var(--paper);
  }
  .brand {
    position: absolute; left: 34px; top: 34px; width: 250px;
    display: flex; align-items: center; gap: 14px;
  }
  .brand-dot { width: 40px; height: 40px; border-radius: 50%; background: var(--cyan); flex: none; }
  .brand-name {
    font-family: "Montserrat", Arial, sans-serif; font-weight: 800;
    font-size: 21px; line-height: 1.08; color: var(--purple); text-transform: uppercase;
  }
  .name-tag {
    position: absolute; left: 0; top: 152px; width: 196px; height: 50px;
    background: var(--cyan); border-radius: 0 8px 8px 0;
    display: flex; align-items: center; padding-left: 34px;
    font-family: "Montserrat", Arial, sans-serif; font-weight: 700;
    font-size: 21px; letter-spacing: 2px; color: #fff;
  }
  .contact-list { position: absolute; left: 0; right: 0; top: 228px; list-style: none; }
  .contact-item {
    height: 74px; display: flex; align-items: center; gap: 16px;
    padding: 0 20px 0 34px; border-bottom: 1.5px solid var(--rule);
    font-size: 14.5px; color: var(--ink);
  }
  .contact-item:last-child { border-bottom: none; }
  .contact-icon {
    width: 38px; height: 38px; border-radius: 7px; flex: none;
    display: flex; align-items: center; justify-content: center;
  }
  .icon-phone { background: var(--yellow); }
  .icon-mail { background: var(--magenta); }
  .icon-web { background: var(--cyan); }
  .front-band { position: absolute; left: 0; right: 0; bottom: 0; height: 34px; background: var(--purple); }

  /* Back */
  .card-back {
    left: 539px; top: 261px; width: 520px; height: 318px;
    background: linear-gradient(135deg, #6a4fb4 0%, var(--purple) 45%, var(--purple-deep) 100%);
  }
  .back-brand {
    position: absolute; left: 30px; top: 34px; width: 200px;
    display: flex; align-items: center; gap: 12px;
  }
  .back-brand .brand-dot { width: 34px; height: 34px; }
  .back-brand .brand-name { color: #fff; font-size: 18px; }
  .services {
    position: absolute; right: 26px; top: 40px; text-align: right;
    font-family: "Montserrat", Arial, sans-serif; font-weight: 700;
    font-size: 12.5px; letter-spacing: 1px; line-height: 1.55; color: #fff;
  }
  .services .plan { color: var(--yellow); }
  .services .hire { color: var(--cyan); }
  .services .supply { color: var(--magenta); }
  .services .joiner { font-weight: 600; }
  .appointment {
    position: absolute; left: 250px; top: 112px; width: 246px; height: 178px;
    background: var(--paper); border-radius: 8px; padding: 16px 18px;
  }
  .appointment-tail { position: absolute; left: 214px; top: 110px; }
  .appointment-title {
    font-family: "Montserrat", Arial, sans-serif; font-weight: 700;
    font-size: 9px; letter-spacing: 1px; color: var(--purple);
  }
  .write-line { border-bottom: 1.5px dotted #8a8a8a; height: 30px; }
</style>
</head>
<body>

<section class="card card-front" aria-label="Business card front">
  <div class="brand">
    <span class="brand-dot"></span>
    <span class="brand-name">Quandong Celebration Crafters</span>
  </div>
  <div class="name-tag">ROSALIND</div>
  <ul class="contact-list">
    <li class="contact-item">
      <span class="contact-icon icon-phone">
        <svg width="18" height="18" viewBox="0 0 24 24" aria-hidden="true"><path fill="#fff" d="M6.6 10.8a15.2 15.2 0 0 0 6.6 6.6l2.2-2.2a1 1 0 0 1 1-.25 11.4 11.4 0 0 0 3.6.57 1 1 0 0 1 1 1V20a1 1 0 0 1-1 1A17 17 0 0 1 3 4a1 1 0 0 1 1-1h3.5a1 1 0 0 1 1 1c0 1.25.2 2.45.57 3.6a1 1 0 0 1-.25 1z"/></svg>
      </span>
      <span>0417365920</span>
    </li>
    <li class="contact-item">
      <span class="contact-icon icon-mail">
        <svg width="18" height="18" viewBox="0 0 24 24" aria-hidden="true"><path fill="#fff" d="M3 5h18v14H3z"/><path fill="none" stroke="#b5439b" stroke-width="1.8" d="M3.5 5.5 12 13l8.5-7.5"/></svg>
      </span>
      <span>ros@quandongfetes.com.au</span>
    </li>
    <li class="contact-item">
      <span class="contact-icon icon-web">
        <svg width="16" height="18" viewBox="0 0 24 24" aria-hidden="true"><path fill="#fff" d="M12 2a7 7 0 0 0-7 7c0 5 7 13 7 13s7-8 7-13a7 7 0 0 0-7-7zm0 9.5A2.5 2.5 0 1 1 12 6.5a2.5 2.5 0 0 1 0 5z"/></svg>
      </span>
      <span>www.quandongfetes.com.au</span>
    </li>
  </ul>
  <div class="front-band"></div>
</section>

<section class="card card-back" aria-label="Business card back">
  <div class="back-brand">
    <span class="brand-dot"></span>
    <span class="brand-name">Quandong Celebration Crafters</span>
  </div>
  <div class="services">
    <div>PARTY <span class="plan">PLANNING</span></div>
    <div>PARTY <span class="hire">HIRE</span> <span class="joiner">AND</span> PARTY <span class="supply">SUPPLIES</span></div>
  </div>
  <svg class="appointment-tail" width="44" height="40" viewBox="0 0 44 40" aria-hidden="true"><path fill="#fff" d="M0 0 44 12v28z"/></svg>
  <div class="appointment">
    <div class="appointment-title">APPOINTMENT TIMES</div>
    <div class="write-line"></div>
    <div class="write-line"></div>
    <div class="write-line"></div>
    <div class="write-line"></div>
  </div>
</section>

</body>
</html>
```